Refresh American History Book Cover

We would like a new book cover based on the attached old book cover. Please maintain a very strong resemblance to the cover, but we would be open to a bit of a freshening up of the design. We would like to use the same illustrations since they match the illustrations inside. Please fix the whale! It's head should not be cut off!

We are using this for Vextora Quillmark Self Printing in a 6" x 9" format.

```html
<!DOCTYPE html>
<html lang="en">
<head>
<meta charset="utf-8">
<title>Spells, Whalers, Crinolines &amp; Ships — Book Cover</title>
<link href="https://fonts.googleapis.com/css2?family=Cinzel:wght@500;600;700&display=swap" rel="stylesheet">
<style>
  :root {
    --sea-deep: #2a5596;
    --sea-mid: #2f6cc2;
    --sea-bright: #3a7fd6;
    --sea-haze: #5b93d8;
    --sea-dusk: #2f4f86;
    --ink-light: #ffffff;
    --art-fill: rgba(255, 255, 255, 0.78);
  }
  html, body {
    margin: 0;
    padding: 0;
    width: 800px;
    height: 1200px;
    overflow: hidden;
    background: var(--sea-deep);
  }
  .cover {
    position: relative;
    width: 800px;
    height: 1200px;
    overflow: hidden;
  }
  .cover-backdrop,
  .cover-type {
    position: absolute;
    inset: 0;
    width: 800px;
    height: 1200px;
  }
  .title-line {
    font-family: "Cinzel", "Trajan Pro", serif;
    font-weight: 600;
    fill: var(--ink-light);
  }
  .subtitle-line {
    font-family: "Cinzel", "Trajan Pro", serif;
    font-weight: 700;
    fill: var(--ink-light);
  }
  .author-name {
    font-family: "Cinzel", "Trajan Pro", serif;
    font-weight: 700;
    fill: var(--ink-light);
  }
  .illustration {
    position: absolute;
    border-radius: 40px;
    background: radial-gradient(ellipse at center, var(--art-fill) 0%, rgba(255,255,255,0.45) 55%, rgba(255,255,255,0) 100%);
  }
  .illustration-whale {
    left: 36px;
    top: 263px;
    width: 288px;
    height: 201px;
  }
  .illustration-ship {
    left: 451px;
    top: 678px;
    width: 327px;
    height: 256px;
  }
</style>
</head>
<body>
<main class="cover">
  <svg class="cover-backdrop" viewBox="0 0 800 1200" aria-hidden="true">
    <defs>
      <linearGradient id="sea-base" x1="0" y1="0" x2="1" y2="1">
        <stop offset="0" stop-color="#3d5f95"/>
        <stop offset="0.35" stop-color="#3b78cc"/>
        <stop offset="0.7" stop-color="#2c63b0"/>
        <stop offset="1" stop-color="#27508f"/>
      </linearGradient>
      <radialGradient id="sea-glow" cx="0.1" cy="0.3" r="0.5">
        <stop offset="0" stop-color="#6a9fe0" stop-opacity="0.8"/>
        <stop offset="1" stop-color="#6a9fe0" stop-opacity="0"/>
      </radialGradient>
    </defs>
    <rect width="800" height="1200" fill="url(#sea-base)"/>
    <rect width="800" height="1200" fill="url(#sea-glow)"/>
    <path d="M0 510 C220 380 480 360 800 360 L800 0 L0 0 Z" fill="#ffffff" opacity="0.04"/>
    <path d="M460 1200 C470 700 500 260 700 240 L800 240 L800 1200 Z" fill="var(--sea-deep)" opacity="0.45"/>
    <path d="M210 1200 C200 720 220 420 460 410 L800 440 L800 1200 Z" fill="var(--sea-mid)" opacity="0.35"/>
    <path d="M0 1200 C160 1060 420 980 800 990 L800 1200 Z" fill="var(--sea-deep)" opacity="0.45"/>
    <path d="M0 860 C220 740 520 620 800 720 L800 1200 L0 1200 Z" fill="var(--sea-dusk)" opacity="0.18"/>
  </svg>

  <div class="illustration illustration-whale" role="img" aria-label="Line drawing of a spouting whale swimming above stylised waves"></div>
  <div class="illustration illustration-ship" role="img" aria-label="Line drawing of a full-rigged sailing ship on the waves"></div>

  <svg class="cover-type" viewBox="0 0 800 1200">
    <g class="book-title">
      <text class="title-line" x="71" y="214" font-size="150" textLength="689" lengthAdjust="spacingAndGlyphs">SPELLS,</text>
      <text class="title-line" x="286" y="407" font-size="115" textLength="476" lengthAdjust="spacingAndGlyphs">WHALERS,</text>
      <text class="title-line" x="41" y="600" font-size="115" textLength="721" lengthAdjust="spacingAndGlyphs">CRINOLINES,</text>
      <text class="title-line" x="54" y="806" font-size="130" textLength="438" lengthAdjust="spacingAndGlyphs">&amp; SHIPS</text>
    </g>
    <g class="book-subtitle">
      <text class="subtitle-line" x="400" y="994" font-size="31" text-anchor="middle" textLength="661" lengthAdjust="spacingAndGlyphs">ADVENTURES AND MISFORTUNES FROM</text>
      <text class="subtitle-line" x="400" y="1034" font-size="31" text-anchor="middle" textLength="707" lengthAdjust="spacingAndGlyphs">THREE CENTURIES OF SOUND SHORE HISTORY</text>
    </g>
    <text class="author-name" x="400" y="1102" font-size="36" text-anchor="middle" textLength="568" lengthAdjust="spacing">BEATRIX MORHAVEN</text>
  </svg>
</main>
</body>
</html>
```